Valtor Holidays Revamp Project 2015

We are a inbound Travel and tour operator based in Kuala Lumpur, Malaysia, established since 2010. Need a vibrant, dynamic, interactive and user friendly, we expect a Content management system for self data upload.
We cater to different markets around the world form Gulf, to the Far East.
Europe to Africa. With the minimum budget we give maximum services.
The final design should communicate well with the user and portray our growth.

Here is the reference of what our current website looks like.
www.valtorholidays-example.com.my

Target Market(s)

Far-East, South East Asia, Gulf market.

Industry/Entity Type

Travel

Number of Pages Required

5+ page

Font styles to use
Serif
Sans Serif
Other font styles liked:
• Calibri

Requirements
Must have
• User interaction, User friendly, Payment integration, should have a fun interface.
Should not have
• Should not have a complicated and overcrowded or jumbled up layout.

```html
<!DOCTYPE html>
<html lang="en">
<head>
<meta charset="utf-8">
<title>Valtor Holidays</title>
<link rel="stylesheet" href="https://fonts.googleapis.com/css2?family=Carlito:wght@400;700&family=Raleway:wght@300;400;600&family=Open+Sans:wght@400&display=swap">
<style>
:root{
  --red:#cc2a30;
  --red-dark:#b81d2a;
  --ink:#1f1f1f;
  --grey:#6b6b6b;
  --line:#cfcfcf;
  --white:#ffffff;
  --black:#000000;
  --teal-1:#1f3b4c;
  --teal-2:#0f2a30;
}
*{margin:0;padding:0;box-sizing:border-box}
html,body{width:692px;height:1200px;overflow:hidden;background:var(--white)}
body{position:relative;font-family:"Carlito","Open Sans",sans-serif;color:var(--ink)}
.abs{position:absolute}

/* hero */
.hero{left:0;top:0;width:692px;height:300px;background:linear-gradient(180deg,#8fb1cf 0%,#a9c3d6 35%,#6aa7b4 58%,#6f8a5c 75%,#8a8a78 100%)}
.brand{left:0;top:26px;width:692px;display:flex;justify-content:center;align-items:center;gap:10px}
.brand-dot{width:26px;height:26px;border-radius:50%;background:var(--red)}
.brand-name{font-family:"Carlito",sans-serif;font-weight:700;font-size:30px;color:var(--ink)}
.nav{left:58px;top:92px;width:577px;height:27px;background:var(--black);display:flex;align-items:center;padding-left:18px}
.nav a{color:var(--white);font-family:"Open Sans",sans-serif;font-size:9.5px;text-decoration:none}
.nav .sep{color:var(--white);font-size:10px;margin:0 11px}
.search{position:absolute;right:9px;top:6px;width:111px;height:14px;background:#1d1d1d;display:flex;justify-content:flex-end;align-items:center;padding-right:4px}
.headline{left:0;top:170px;width:692px;text-align:center;font-family:"Carlito",sans-serif;font-size:35px;color:var(--white);text-shadow:0 1px 3px rgba(0,0,0,.35)}
.request{left:187px;top:215px;width:340px;height:54px;background:rgba(255,255,255,.25)}
.request-field{left:197px;top:224px;width:210px;height:35px;background:var(--white);border-radius:2px;font-family:"Open Sans",sans-serif;font-size:9.5px;color:#9a9a9a;padding:9px 0 0 10px}
.request-btn{left:413px;top:224px;width:105px;height:35px;background:var(--red-dark);border-radius:4px;color:var(--white);font-size:16px;text-align:center;line-height:35px}

/* section headings */
.heading{left:0;width:692px;text-align:center}
.rule{height:1px}
.rule i{position:absolute;top:-1px;height:3px;width:32px}

/* packages */
.packages-title{top:320px;font-family:"Raleway",sans-serif;font-weight:300;font-size:21px;color:#555}
.packages-rule{left:254px;top:360px;width:180px;background:var(--line)}
.packages-rule i{left:64px;background:var(--ink)}
.package{width:171px;height:47px;border:1px solid #222;border-radius:3px;display:flex;align-items:center;justify-content:center;font-family:"Raleway",sans-serif;font-size:12.5px;color:#222}

/* gallery */
.gallery{left:0;top:484px;width:692px;height:244px;background:var(--red)}
.gallery-title{top:500px;font-family:"Raleway",sans-serif;font-weight:600;font-size:21px;color:var(--white)}
.gallery-rule{left:244px;top:535px;width:179px;background:rgba(255,255,255,.8)}
.gallery-rule i{left:73px;background:var(--white)}
.tile{width:161px;height:104px;border:2px solid var(--white)}
.tile-label{width:161px;text-align:center;font-family:"Raleway",sans-serif;font-weight:600;font-size:13.5px;color:var(--white)}

/* testimonials */
.testimonials{left:0;top:728px;width:692px;height:238px;background:linear-gradient(180deg,var(--teal-1) 0%,#15262c 55%,#1d4a57 85%,#2b6475 100%)}
.testimonials-title{top:750px;font-family:"Raleway",sans-serif;font-weight:600;font-size:24px;color:var(--white)}
.testimonials-rule{left:251px;top:791px;width:179px;background:rgba(255,255,255,.6)}
.testimonials-rule i{left:74px;background:var(--white)}
.quote-mark{left:56px;top:808px;font-family:Georgia,serif;font-size:42px;line-height:1;color:#555}
.quote{left:84px;top:815px;width:524px;text-align:center;font-family:"Open Sans",sans-serif;font-size:8.3px;line-height:14px;color:var(--white)}
.avatar{left:264px;top:880px;width:43px;height:43px;border-radius:50%;border:2px solid var(--white);background:linear-gradient(135deg,#9a9a9a,#4b4b4b)}
.author{left:317px;top:893px;font-family:"Open Sans",sans-serif;font-size:7.5px;line-height:11px}
.author .name{color:var(--red)}
.author .role{color:var(--white);font-weight:700}

/* contact */
.contact{left:0;top:985px;width:692px;text-align:center;font-family:"Carlito",sans-serif;font-size:12px;line-height:20px;color:var(--grey)}
.contact b{color:var(--ink);font-weight:400}
.contact .stars{color:#555;font-size:10px;letter-spacing:.5px;line-height:18px}
.contact .copy{color:var(--ink);font-size:11px}
</style>
</head>
<body>

<header class="abs hero" role="img" aria-label="Tropical resort photo: palm trees, pool and sea beneath a blue sky"></header>
<div class="abs brand"><span class="brand-dot"></span><span class="brand-name">Valtor Holidays</span></div>

<nav class="abs nav">
  <a href="#">Agents</a><span class="sep">|</span>
  <a href="#">My Booking</a><span class="sep">|</span>
  <a href="#">Destinations</a><span class="sep">|</span>
  <a href="#">Travel offers</a>
  <div class="search">
    <svg width="10" height="10" viewBox="0 0 10 10"><circle cx="4" cy="4" r="3" fill="none" stroke="#fff" stroke-width="1.4"/><line x1="6.2" y1="6.2" x2="9" y2="9" stroke="#fff" stroke-width="1.6"/></svg>
  </div>
</nav>

<h1 class="abs headline" style="font-weight:400">Travel With Us With Best Deal</h1>
<div class="abs request"></div>
<div class="abs request-field">Request for Services</div>
<div class="abs request-btn">Submit Now !</div>

<h2 class="abs heading packages-title">Most Popular Packages</h2>
<div class="abs rule packages-rule"><i></i></div>
<div class="abs package" style="left:69px;top:390px">3 nights malaysia package</div>
<div class="abs package" style="left:254px;top:389px">5 nights malaysia package</div>
<div class="abs package" style="left:438px;top:388px">7 nights malaysia package</div>

<section class="abs gallery"></section>
<h2 class="abs heading gallery-title">Our Gallery</h2>
<div class="abs rule gallery-rule"><i></i></div>
<div class="abs tile" style="left:76px;top:573px;background:linear-gradient(180deg,#3f7fd0 0%,#9fc2e8 45%,#8a94a0 70%,#3d6b3a 100%)" role="img" aria-label="City skyline photo with towers under a blue sky"></div>
<div class="abs tile" style="left:257px;top:573px;background:linear-gradient(180deg,#2a86d6 0%,#86c7ef 40%,#4fd0d0 65%,#efe6cf 100%)" role="img" aria-label="Tropical beach photo with turquoise water and white sand"></div>
<div class="abs tile" style="left:438px;top:573px;background:linear-gradient(180deg,#6fa9d8 0%,#b9d6ea 30%,#7a5a48 50%,#2fb7a7 75%,#1f6e6a 100%)" role="img" aria-label="Water villas on stilts above a clear lagoon"></div>
<div class="abs tile-label" style="left:69px;top:685px">Product 1</div>
<div class="abs tile-label" style="left:259px;top:685px">Product 2</div>
<div class="abs tile-label" style="left:432px;top:685px">Product 3</div>

<section class="abs testimonials" role="img" aria-label="Dim photo of palm leaves over the sea at dusk"></section>
<h2 class="abs heading testimonials-title">Testimonials</h2>
<div class="abs rule testimonials-rule"><i></i></div>
<div class="abs quote-mark">&ldquo;</div>
<p class="abs quote">Lorem ipsum dolor sit amet, consectetur adipisicing elit, sed do eiusmod tempor incididunt ut labore et dolore magna aliqua. Ut enim ad minim veniam, quis nostrud exercitation ullamco laboris nisi ut aliquip Ut enim ad minim veniam, quis nostrud.consectetur adipisicing elit, sed do eiusmod tempor We strive to maintain the highest standards while exceed.Ut enim ad minim veniam, quis nostrud exercitation ullamco laboris nisi ut aliquip Ut enim ad minim veniam, quis nostrud.consectetur adipisicing aliqua.</p>
<div class="abs avatar" role="img" aria-label="Portrait photo of the reviewer"></div>
<div class="abs author"><div class="name">Marlo Fenwick</div><div class="role">chairman</div></div>

<footer class="abs contact">
  <svg width="18" height="25" viewBox="0 0 18 25" aria-hidden="true"><path d="M9 0C4 0 0 4 0 9c0 6.5 9 16 9 16s9-9.5 9-16C18 4 14 0 9 0z" fill="#cc2a30"/><circle cx="9" cy="9" r="3.4" fill="#fff"/></svg>
  <div style="margin-top:6px"><b>Head Office:</b> Suite No. 8</div>
  <div>No.42 Jalan Seri Melati Kuala Lumpur . Malaysia.</div>
  <div>Suite No. 306, 3rd Floor Harwin Centre Shahrah</div>
  <div>T: +603 21110457</div>
  <div><b>E:</b> Tours@valtorholidays-example.com.my</div>
  <div><b>W:</b> www.valtorholidays-example.com.my</div>
  <div class="stars">******************************************</div>
  <div class="copy">Copyright © 2014 All Right Reserved, Valtor holidays.</div>
</footer>

</body>
</html>
```